business card for a shoe shop

we would like a business card for a family owned shoe shop.
With this information included.
Dunleavy's Shoe Store
Family owned since 1947

then on other side
Dunleavy's Shoe Store
Footwear fitting specialist
Phone: 9471 2386
218 Tarn St, Wexley Heights 3091
(cnr. Corrigan Rd and Tarn St)
dunleavyshoes218@quillmail.example
if could incorporate the purple color on card i have attached.

```html
<!DOCTYPE html>
<html lang="en">
<head>
<meta charset="utf-8">
<title>Dunleavy's Shoe Store — Business Card</title>
<link rel="stylesheet" href="https://fonts.googleapis.com/css2?family=Josefin+Sans:wght@400&family=Poppins:wght@400&family=Courgette&display=swap">
<style>
  :root {
    --backdrop: #d6d6d6;
    --brand-purple: #7156a6;
    --card-white: #ffffff;
    --ink: #1f1f1f;
    --soft-white: #f3effa;
  }
  html, body {
    margin: 0;
    padding: 0;
    width: 1200px;
    height: 852px;
    overflow: hidden;
    background: var(--backdrop);
  }
  .canvas {
    position: relative;
    width: 1200px;
    height: 852px;
  }
  .card {
    position: absolute;
    top: 272px;
    width: 540px;
    height: 308px;
    border-radius: 22px;
    overflow: hidden;
    box-shadow: 0 6px 18px rgba(0,0,0,0.18);
  }
  /* Front face */
  .card--front {
    left: 40px;
    background: var(--brand-purple);
    color: var(--card-white);
  }
  .front__brand {
    position: absolute;
    top: 96px;
    left: 0;
    width: 100%;
    text-align: center;
    font-family: "Josefin Sans", sans-serif;
    font-weight: 400;
    font-size: 40px;
    line-height: 1.15;
    letter-spacing: 0.5px;
    color: var(--card-white);
  }
  .front__tagline {
    position: absolute;
    bottom: 48px;
    left: 0;
    width: 100%;
    text-align: center;
    font-family: "Josefin Sans", sans-serif;
    font-size: 13px;
    letter-spacing: 0.4px;
    color: var(--soft-white);
  }
  /* Back face */
  .card--back {
    left: 620px;
    background: var(--card-white);
    color: var(--ink);
  }
  .back__brand {
    position: absolute;
    top: 30px;
    left: 0;
    width: 100%;
    text-align: center;
    font-family: "Josefin Sans", sans-serif;
    font-weight: 400;
    font-size: 32px;
    line-height: 1.15;
    color: var(--brand-purple);
  }
  .back__address {
    position: absolute;
    top: 128px;
    right: 26px;
    text-align: right;
    font-family: "Poppins", sans-serif;
    font-size: 12.5px;
    line-height: 1.5;
    color: var(--ink);
  }
  .back__band {
    position: absolute;
    left: 0;
    width: 100%;
    background: var(--brand-purple);
  }
  .back__band--tagline {
    top: 172px;
    height: 30px;
  }
  .back__tagline {
    display: block;
    padding-left: 28px;
    font-family: "Courgette", cursive;
    font-size: 17px;
    line-height: 30px;
    color: var(--card-white);
  }
  .back__band--lower {
    top: 222px;
    height: 12px;
  }
  .back__contacts {
    position: absolute;
    left: 26px;
    bottom: 22px;
    margin: 0;
    padding: 0;
    list-style: none;
    font-family: "Poppins", sans-serif;
    font-size: 13px;
    color: var(--ink);
  }
  .contact-item {
    display: flex;
    align-items: center;
    gap: 8px;
    line-height: 22px;
  }
  .contact-icon {
    width: 13px;
    height: 13px;
    flex: none;
  }
</style>
</head>
<body>
<main class="canvas">

  <section class="card card--front" aria-label="Business card front">
    <div class="front__brand">Dunleavy's<br>Shoe Store</div>
    <p class="front__tagline" style="margin:0">Family owned since 1947</p>
  </section>

  <section class="card card--back" aria-label="Business card back">
    <div class="back__brand">Dunleavy's<br>Shoe Store</div>

    <p class="back__address" style="margin:0">
      218 Tarn St, Wexley Heights 3091<br>
      (cnr. Corrigan Rd and Tarn St)
    </p>

    <div class="back__band back__band--tagline">
      <span class="back__tagline">Footwear fitting specialist</span>
    </div>
    <div class="back__band back__band--lower"></div>

    <ul class="back__contacts">
      <li class="contact-item">
        <svg class="contact-icon" viewBox="0 0 16 16" aria-hidden="true">
          <circle cx="8" cy="8" r="8" fill="var(--brand-purple)"/>
          <path d="M5.2 4.2l1.4-.3.8 1.9-1 .8c.5 1.1 1.3 1.9 2.4 2.4l.8-1 1.9.8-.3 1.4c-3.3.2-6.2-2.7-6-6z" fill="#fff"/>
        </svg>
        <span>9471 2386</span>
      </li>
      <li class="contact-item">
        <svg class="contact-icon" viewBox="0 0 16 16" aria-hidden="true">
          <rect x="0" y="2" width="16" height="12" fill="var(--brand-purple)"/>
          <path d="M1 3.5l7 5.5 7-5.5" fill="none" stroke="#fff" stroke-width="1.3"/>
        </svg>
        <span>dunleavyshoes218@quillmail.example</span>
      </li>
    </ul>
  </section>

</main>
</body>
</html>
```